Business Card Design for L & W Manufacturing
L & W Manfacturing
Business Card Design for L & W Manufacturing -
Creative Brief
Professional
Derek Halvorsen
President
20457 Cedar Lane Southeast Elk Harbor, MN 55418
dhalvorsen@lnwfabworks.com
www.lnwfabworks.com
I need someone to fix the spelling error that is in the "Accurate Parts and Crafted Solutions" text...precision is missing the "P". I want the list of items on the back of the card to be stacked and aligned vertically.
CNC and Manual Milling, Lathe Turning, Custom Welding, DraftForge CAD Software, Automation Equipment Design and Fabrication
kelpir kelpir
This note is for all the designers. Please use all capitals and the same text font that is found in the logo design...this is for ALL text on the business card. Also, please be sure to remove the commas on back of the card, these should not be on the final design. Finally, I want "PHONE", "MOBILE, and "FAX" spelled out on the card. Really like the concepts and please keep them coming! Thanks!

```html
<!DOCTYPE html>
<html lang="en">
<head>
<meta charset="utf-8">
<title>L &amp; W Manufacturing Stationery</title>
<link rel="stylesheet" href="https://fonts.googleapis.com/css2?family=Arimo:wght@400;700&display=swap">
<style>
  :root {
    --stage: #a7a8aa;
    --paper: #ffffff;
    --navy-deep: #061a33;
    --navy: #0d3566;
    --blue-glow: #2c6fb0;
    --brand-blue: #1c4f8c;
    --ink: #222222;
    --ink-soft: #555555;
  }
  * { box-sizing: border-box; margin: 0; padding: 0; }
  html, body { width: 1200px; height: 756px; overflow: hidden; }
  body {
    position: relative;
    background: var(--stage);
    font-family: "Arimo", Arial, sans-serif;
    color: var(--ink);
    text-transform: uppercase;
  }
  .band {
    background: radial-gradient(ellipse at 50% 20%, var(--blue-glow) 0%, var(--navy) 45%, var(--navy-deep) 100%);
  }
  .wordmark {
    display: flex; align-items: center; gap: 5px;
    color: var(--brand-blue); font-weight: 400; letter-spacing: 0.04em; white-space: nowrap;
  }
  .wordmark .dot { border-radius: 50%; background: var(--brand-blue); flex: none; }
  .tagline { color: var(--ink-soft); letter-spacing: 0.06em; white-space: nowrap; }

  /* Letterhead */
  .letterhead {
    position: absolute; left: 19px; top: 12px; width: 504px; height: 727px;
    background: var(--paper);
  }
  .letterhead .band { position: absolute; left: 0; top: 0; width: 100%; height: 62px; }
  .letterhead .brand {
    position: absolute; left: 0; right: 0; top: 92px;
    display: flex; flex-direction: column; align-items: center; gap: 3px;
  }
  .letterhead .wordmark { font-size: 15px; }
  .letterhead .wordmark .dot { width: 12px; height: 12px; }
  .letterhead .tagline { font-size: 5px; }
  .footer-lines {
    position: absolute; left: 0; right: 0; font-size: 5.5px; text-align: center; line-height: 1.6;
  }
  .letterhead .footer-lines { bottom: 18px; }

  /* Business cards */
  .card {
    position: absolute; left: 175px; width: 283px; height: 125px;
    border: 1px solid #d4d4d4; overflow: hidden;
  }
  .card-front { top: 307px; background: var(--paper); }
  .card-front .band { position: absolute; left: 0; top: 0; width: 100%; height: 36px; }
  .card-front .brand {
    position: absolute; left: 0; right: 0; top: 42px;
    display: flex; flex-direction: column; align-items: center; gap: 2px;
  }
  .card-front .wordmark { font-size: 12px; }
  .card-front .wordmark .dot { width: 9px; height: 9px; }
  .card-front .tagline { font-size: 4px; }
  .card-front .holder { position: absolute; left: 0; right: 0; top: 73px; text-align: center; font-size: 5.5px; }
  .card-front .holder strong { font-weight: 700; }
  .card-front .contact {
    position: absolute; left: 0; right: 0; top: 86px; text-align: center; font-size: 4px; line-height: 1.6;
  }
  .card-back { top: 439px; height: 127px; }
  .card-back .services {
    list-style: none; position: absolute; left: 16px; top: 24px;
    color: #e6eef8; font-size: 6px; line-height: 1.7;
  }
  .card-back .web {
    position: absolute; left: 0; right: 0; bottom: 10px; text-align: center; color: #dbe6f3; font-size: 4.5px;
    text-transform: lowercase;
  }

  /* Envelopes */
  .envelope {
    position: absolute; left: 557px; width: 619px; height: 283px; background: var(--paper); overflow: hidden;
  }
  .envelope-back { top: 72px; }
  .envelope-back svg { position: absolute; left: 0; top: 0; }
  .envelope-back .web {
    position: absolute; left: 0; right: 0; top: 72px; text-align: center; color: #dbe6f3; font-size: 6px;
    text-transform: lowercase;
  }
  .envelope-front { top: 384px; }
  .envelope-front .band { position: absolute; left: 0; top: 0; width: 100%; height: 84px; }
  .envelope-front .brand {
    position: absolute; left: 0; right: 0; top: 104px;
    display: flex; flex-direction: column; align-items: center; gap: 3px;
  }
  .envelope-front .wordmark { font-size: 15px; }
  .envelope-front .wordmark .dot { width: 12px; height: 12px; }
  .envelope-front .tagline { font-size: 5px; }
  .envelope-front .footer-lines { bottom: 34px; }
</style>
</head>
<body>

<section class="letterhead">
  <div class="band"></div>
  <div class="brand">
    <div class="wordmark"><span class="dot"></span>L &amp; W Manufacturing</div>
    <div class="tagline">Accurate Parts and Crafted Solutions</div>
  </div>
  <div class="footer-lines">
    <p><b>Address:</b> 20457 Cedar Lane Southeast Elk Harbor, MN 55418 | <b>Email:</b> dhalvorsen@lnwfabworks.com | <b>Web:</b> www.lnwfabworks.com</p>
    <p><b>Phone:</b> (218) 555-0142 | <b>Mobile:</b> (218) 555-0187 | <b>Fax:</b> (218) 555-0163</p>
  </div>
</section>

<section class="card card-front">
  <div class="band"></div>
  <div class="brand">
    <div class="wordmark"><span class="dot"></span>L &amp; W Manufacturing</div>
    <div class="tagline">Accurate Parts and Crafted Solutions</div>
  </div>
  <p class="holder"><strong>Derek Halvorsen</strong> | President</p>
  <div class="contact">
    <p>Address: 20457 Cedar Lane Southeast Elk Harbor, MN 55418</p>
    <p>Email: dhalvorsen@lnwfabworks.com | Web: www.lnwfabworks.com</p>
    <p>Phone: (218) 555-0142 | Mobile: (218) 555-0187 | Fax: (218) 555-0163</p>
  </div>
</section>

<section class="card card-back band">
  <ul class="services">
    <li>CNC and Manual Milling</li>
    <li>Lathe Turning</li>
    <li>Custom Welding</li>
    <li>DraftForge CAD Software</li>
    <li>Automation Equipment Design and Fabrication</li>
  </ul>
  <p class="web">www.lnwfabworks.com</p>
</section>

<section class="envelope envelope-back">
  <svg width="619" height="283" viewBox="0 0 619 283" aria-hidden="true">
    <defs>
      <radialGradient id="flapGlow" cx="50%" cy="30%" r="70%">
        <stop offset="0" stop-color="#2c6fb0"/>
        <stop offset="0.5" stop-color="#0d3566"/>
        <stop offset="1" stop-color="#061a33"/>
      </radialGradient>
    </defs>
    <path d="M0 0 H619 V80 Q619 165 535 165 H84 Q0 165 0 80 Z" fill="url(#flapGlow)"/>
  </svg>
  <p class="web">www.lnwfabworks.com</p>
</section>

<section class="envelope envelope-front">
  <div class="band"></div>
  <div class="brand">
    <div class="wordmark"><span class="dot"></span>L &amp; W Manufacturing</div>
    <div class="tagline">Accurate Parts and Crafted Solutions</div>
  </div>
  <div class="footer-lines">
    <p><b>Address:</b> 20457 Cedar Lane Southeast Elk Harbor, MN 55418 | <b>Email:</b> dhalvorsen@lnwfabworks.com | <b>Web:</b> www.lnwfabworks.com</p>
    <p><b>Phone:</b> (218) 555-0142 | <b>Mobile:</b> (218) 555-0187 | <b>Fax:</b> (218) 555-0163</p>
  </div>
</section>

</body>
</html>
```